International Trading Company, 'KIRO' needs a Business Card

The company name is "KIRO" and it has own logo design.
I'd like to use its logo on this business card.
I need two side Business Card.
I'll look forward to your great design.
Thank you very much in advance.

Contact Information for Business Card

Company Name : Kiro Harbour Limited
Information Example
Dorian Pallister
Mobile(use icon please) : 1 (212) 555-0143
Tel(use icon please) : 1 (212) 555-0178
Email(use icon please) : dorian27@kiroharbour-mail.com
Address(use icon please) : 482 Halden Ave, New York, NY 10160, USA

```html
<!DOCTYPE html>
<html lang="en">
<head>
<meta charset="utf-8">
<title>Kiro Harbour Limited – Business Card</title>
<link href="https://fonts.googleapis.com/css2?family=Lato:wght@300;400;700;900&display=swap" rel="stylesheet">
<style>
  :root {
    --stage: #e6e6e4;
    --card-dark: #232323;
    --card-light: #ffffff;
    --ink: #2b2b2b;
    --ink-soft: #555555;
    --mark-grey: #7a7a7a;
    --mark-dark: #5c5c5c;
    --rule: #3a3a3a;
  }
  * { margin: 0; padding: 0; box-sizing: border-box; }
  html, body { width: 1200px; height: 878px; overflow: hidden; }
  body {
    background: var(--stage);
    font-family: 'Lato', sans-serif;
    position: relative;
  }
  .card {
    position: absolute;
    top: 290px;
    width: 520px;
    height: 298px;
    box-shadow: 0 6px 18px rgba(0,0,0,0.18);
  }
  /* Back side */
  .card-back {
    left: 50px;
    background: var(--card-dark);
    display: flex;
    flex-direction: column;
    align-items: center;
    justify-content: center;
  }
  .back-wordmark {
    font-family: 'Lato', sans-serif;
    font-weight: 900;
    font-size: 96px;
    letter-spacing: 4px;
    color: var(--mark-dark);
    line-height: 1;
  }
  .back-company {
    margin-top: 8px;
    font-weight: 400;
    font-size: 16px;
    letter-spacing: 9px;
    text-transform: uppercase;
    color: #111111;
  }
  /* Front side */
  .card-front {
    left: 630px;
    background: var(--card-light);
  }
  .front-wordmark {
    position: absolute;
    top: 26px;
    right: 30px;
    font-weight: 900;
    font-size: 58px;
    letter-spacing: 2px;
    color: var(--mark-grey);
    line-height: 1;
  }
  .holder {
    position: absolute;
    top: 104px;
    left: 22px;
    padding-left: 16px;
    border-left: 7px solid var(--mark-grey);
  }
  .holder-name {
    font-size: 22px;
    font-weight: 300;
    color: var(--ink);
    line-height: 1.1;
  }
  .holder-name strong { font-weight: 700; }
  .holder-title {
    font-size: 15px;
    font-weight: 400;
    color: var(--ink-soft);
    margin-top: 3px;
  }
  .contact-list {
    position: absolute;
    left: 44px;
    top: 168px;
    list-style: none;
  }
  .contact-item {
    display: flex;
    align-items: center;
    gap: 10px;
    font-size: 15px;
    color: var(--ink);
    height: 23px;
  }
  .contact-item svg { width: 13px; height: 13px; flex: none; fill: var(--ink-soft); }
  .footer-rule {
    position: absolute;
    left: 44px;
    right: 150px;
    bottom: 22px;
    height: 2px;
    background: var(--rule);
  }
  .website {
    position: absolute;
    right: 18px;
    bottom: 15px;
    font-size: 13px;
    color: var(--ink);
  }
</style>
</head>
<body>
  <section class="card card-back" aria-label="Business card back">
    <div class="back-wordmark">KIRO</div>
    <div class="back-company">Kiro Harbour Limited</div>
  </section>

  <section class="card card-front" aria-label="Business card front">
    <div class="front-wordmark">KIRO</div>

    <div class="holder">
      <div class="holder-name">Dorian <strong>Pallister</strong></div>
      <div class="holder-title">Job title</div>
    </div>

    <ul class="contact-list">
      <li class="contact-item">
        <svg viewBox="0 0 16 16" aria-hidden="true"><path d="M4 0h8a1 1 0 0 1 1 1v14a1 1 0 0 1-1 1H4a1 1 0 0 1-1-1V1a1 1 0 0 1 1-1zm1 2v10h6V2zm3 11a1 1 0 1 0 0 2 1 1 0 0 0 0-2z"/></svg>
        (212) 555-0143
      </li>
      <li class="contact-item">
        <svg viewBox="0 0 16 16" aria-hidden="true"><path d="M1 5c0-2 3-3 7-3s7 1 7 3v1h-4V5H5v1H1zm3 2h8l2 7H2zm4 1.5a2 2 0 1 0 0 4 2 2 0 0 0 0-4z"/></svg>
        1 (212) 555-0178
      </li>
      <li class="contact-item">
        <svg viewBox="0 0 16 16" aria-hidden="true"><path d="M0 3h16v10H0zm1.5 1.2v.3L8 9l6.5-4.5v-.3z"/></svg>
        dorian27@kiroharbour-mail.com
      </li>
      <li class="contact-item">
        <svg viewBox="0 0 16 16" aria-hidden="true"><path d="M8 0a5.5 5.5 0 0 0-5.5 5.5C2.5 10 8 16 8 16s5.5-6 5.5-10.5A5.5 5.5 0 0 0 8 0zm0 3.5a2 2 0 1 1 0 4 2 2 0 0 1 0-4z"/></svg>
        482 Halden Ave, New York, NY 10160, USA
      </li>
    </ul>

    <div class="footer-rule"></div>
    <div class="website">kiroharbour-web.com</div>
  </section>
</body>
</html>
```